Face cream packaging | Cosmetic start-up

This project is about creating design proposals for two different types of packaging. Once to a cream jar made of glass and once to a jar made of plastic.
Three different designs must be created for each type of jar. Later, the different packaging will be used as customization options in an online store for cosmetics.

- The packaging variant made of glass should have color gradients. Three different shades are to be chosen. (Preferably with the primary colors red, blue and green). Note: The designer can create other proposals at will if he has better ideas. The logo must be included in some form. (Link to manufacturer description: https://catalogue.valdorpackaging.com/en/portals/valdorpackaging/assets/12667188/lou-50-ml/)

- With the plastic type of packaging, the designer has a lot of freedom to design. The only requirement is that the design must be artistic. It doesn't matter whether abstract patterns, geometric figures, mandalas or just a basic color is chosen. The main thing is that the packaging inspires. The logo must be included in some form. (Link to manufacturer description: https://catalogue.valdorpackaging.com/en/portals/valdorpackaging/assets/12667181/edda-50-ml/)

Thank you in advance for your work and best regards
Olaf

Target Market(s)

Young people with an affinity for social media and the web. Focus is on the female clientele.

Industry/Entity Type

Cosmetics

Font styles to use
Script

Colors
eea4c8
f59195
85cae6
cadf82

Requirements
Must have
• The logo must be included in some form. (PNG-File attached)
Nice to have
• Other types of packaging (can shape, packaging material)

```html
<!DOCTYPE html>
<html lang="en">
<head>
<meta charset="utf-8">
<title>Sola Skin – Face Cream Label Proposals</title>
<link rel="stylesheet" href="https://fonts.googleapis.com/css2?family=Source+Sans+3:wght@300;400&display=swap">
<style>
  :root {
    --page: #ffffff;
    --ink: #2b2b2b;
    --lime-top: #eef68a;
    --lime-mid: #74e2d8;
    --lime-bottom: #88ea86;
    --aqua-top: #f7f3f7;
    --aqua-mid: #90e6e6;
    --aqua-bottom: #3a9fbe;
    --violet-top: #7a3cf2;
    --violet-mid: #c68ad8;
    --violet-bottom: #f7cadb;
    --veil: rgba(255, 255, 255, 0.38);
  }
  * { box-sizing: border-box; margin: 0; padding: 0; }
  html, body { width: 783px; height: 1200px; overflow: hidden; background: var(--page); }
  body { position: relative; font-family: "Source Sans 3", "Myriad Pro", sans-serif; color: var(--ink); }

  .label { position: absolute; left: 0; width: 783px; height: 80px; overflow: hidden; }
  .label--lime   { top: 206px;  background: linear-gradient(180deg, var(--lime-top) 0%, var(--lime-mid) 50%, var(--lime-bottom) 100%); }
  .label--aqua   { top: 608px;  background: linear-gradient(180deg, var(--aqua-top) 0%, var(--aqua-mid) 50%, var(--aqua-bottom) 100%); }
  .label--violet { top: 1006px; width: 778px; background: linear-gradient(180deg, var(--violet-top) 0%, var(--violet-mid) 50%, var(--violet-bottom) 100%); }

  .label__ribbons {
    position: absolute; top: 0; height: 80px; left: 80px; width: 440px;
    background: linear-gradient(110deg, transparent 0%, var(--veil) 30%, transparent 55%, var(--veil) 80%, transparent 100%);
  }

  .label__claim, .label__volume, .label__ingredients, .label__product {
    position: absolute; font-size: 7.6px; line-height: 9.6px; font-weight: 400;
  }
  .label__claim { top: 31px; width: 60px; }
  .label__volume { top: 38px; }
  .label__ingredients { top: 5px; width: 110px; }
  .label__product { font-weight: 300; top: 68px; }

  .brand { position: absolute; top: 10px; width: 125px; }
  .brand__name { font-family: "Source Sans 3", sans-serif; font-weight: 300; font-size: 24px; line-height: 28px; letter-spacing: 1px; color: var(--ink); }
  .brand__rule { display: block; margin-top: 20px; width: 120px; height: 1px; background: var(--ink); }
</style>
</head>
<body>

  <section class="label label--lime">
    <div class="label__ribbons" role="img" aria-label="Flowing translucent ribbon decoration"></div>
    <p class="label__claim" style="left:183px">Lorem ipsum dolor sit amet, consectetuer</p>
    <div class="brand" style="left:314px">
      <p class="brand__name">Sola Skin</p>
      <span class="brand__rule" style="margin-left:23px"></span>
    </div>
    <p class="label__product" style="left:335px">Face Cream</p>
    <p class="label__volume" style="left:518px">50 ml</p>
    <p class="label__ingredients" style="left:605px">Ingredients<br>&nbsp;dolor sit amet, consectetuer adipiscing elit, sed diam nonummy nibh euismod tinci-dunt ut laoreet dolore magna aliquam erat volutpat. Ut wisi enim ad minim veniam, quis</p>
  </section>

  <section class="label label--aqua">
    <div class="label__ribbons" role="img" aria-label="Flowing translucent ribbon decoration"></div>
    <p class="label__claim" style="left:184px">Lorem ipsum dolor sit amet, consectetuer</p>
    <div class="brand" style="left:292px">
      <p class="brand__name">Sola Skin</p>
      <span class="brand__rule" style="margin-left:22px"></span>
    </div>
    <p class="label__product" style="left:349px">Face Cream</p>
    <p class="label__volume" style="left:515px">50 ml</p>
    <p class="label__ingredients" style="left:611px">Ingredients<br>&nbsp;dolor sit amet, consectetuer adipiscing elit, sed diam nonummy nibh euismod tinci-dunt ut laoreet dolore magna aliquam erat volutpat. Ut wisi enim ad minim veniam, quis</p>
  </section>

  <section class="label label--violet">
    <div class="label__ribbons" role="img" aria-label="Flowing translucent ribbon decoration"></div>
    <p class="label__claim" style="left:206px">Lorem ipsum dolor sit amet, consectetuer</p>
    <div class="brand" style="left:331px">
      <p class="brand__name">Sola Skin</p>
      <span class="brand__rule" style="margin-left:23px"></span>
    </div>
    <p class="label__product" style="left:353px">Face Cream</p>
    <p class="label__volume" style="left:533px">50 ml</p>
    <p class="label__ingredients" style="left:612px">Ingredients<br>&nbsp;dolor sit amet, consectetuer adipiscing elit, sed diam nonummy nibh euismod tinci-dunt ut laoreet dolore magna aliquam erat volutpat. Ut wisi enim ad minim veniam, quis</p>
  </section>

</body>
</html>
```